Road Construction Company needs business cards

We would like a new business card designed for our business.

We're a road construction company based in Qld, Australia.

Can the business card please have the following information on it.

Name: Brent Malvoy
Position: General Manager
Phone: 0471 592 304
Email: Brent.malvoy@quendix.com.au
Address: 87 Harrowgate Ave, Pindarra, QLD, 4000
Website: www.quendix.com.au

Visually we'd like the card to be professional and simple.

Attached is our logo.

Our website is www.quendix.com.au

Target Market(s)

Men aged 25-60

Contact Information for Business Card

As listed in project description

Font styles to use
Serif

Requirements
Must have
• Large logo on back of card

```html
<!DOCTYPE html>
<html lang="en">
<head>
<meta charset="utf-8">
<title>Brent Malvoy – Business Card</title>
<link rel="stylesheet" href="https://fonts.googleapis.com/css2?family=Alegreya:ital,wght@0,400;1,700&display=swap">
<style>
  :root {
    --card-bg: #ffffff;
    --ink: #1c1c1c;
    --navy-light: #233a66;
    --navy-dark: #0e1c3a;
  }
  html, body {
    margin: 0;
    padding: 0;
    overflow: hidden;
    background: var(--card-bg);
  }
  .card {
    position: relative;
    width: 1200px;
    height: 735px;
    background: var(--card-bg);
    overflow: hidden;
    font-family: "Alegreya", Georgia, serif;
    color: var(--ink);
  }
  .hex-band {
    position: absolute;
    left: 0;
    top: 0;
    width: 370px;
    height: 735px;
  }
  .identity {
    position: absolute;
    left: 464px;
    top: 138px;
  }
  .identity .name {
    margin: 0;
    font-size: 52px;
    font-weight: 700;
    font-style: italic;
    line-height: 1;
  }
  .identity .role {
    margin: 6px 0 0;
    font-size: 35px;
    font-weight: 400;
    line-height: 1.1;
  }
  .contact {
    position: absolute;
    left: 464px;
    top: 466px;
    margin: 0;
    padding: 0;
    list-style: none;
    font-size: 30px;
    line-height: 42px;
  }
</style>
</head>
<body>
  <div class="card">
    <svg class="hex-band" viewBox="0 0 370 735" role="img" aria-label="Dark navy geometric hexagon texture panel">
      <defs>
        <linearGradient id="navyFill" x1="0" y1="0" x2="1" y2="1">
          <stop offset="0" stop-color="var(--navy-light)"/>
          <stop offset="1" stop-color="var(--navy-dark)"/>
        </linearGradient>
      </defs>
      <polygon fill="url(#navyFill)"
        points="0,0 300,0 366,145 295,281 206,281 122,370 206,459 295,459 366,591 305,735 0,735"/>
    </svg>

    <div class="identity">
      <h1 class="name">Brent Malvoy</h1>
      <p class="role">General Manager</p>
    </div>

    <ul class="contact">
      <li class="phone">0471 592 304</li>
      <li class="email">Brent.malvoy@quendix.com.au</li>
      <li class="address">87 Harrowgate Ave, Pindarra, QLD, 4000</li>
      <li class="web">www.quendix.com.au</li>
    </ul>
  </div>
</body>
</html>
```